ridge-mosaic builders & interiors

I need a web design for my company we offer counter tops. tile for floors,showers,kitchen backsplashes and more also need a place where the client
can write reviews

Industry/Entity Type

Tile

```html
<!DOCTYPE html>
<html lang="en">
<head>
<meta charset="utf-8">
<title>Ridge-Mosaic Builders &amp; Interiors</title>
<link href="https://fonts.googleapis.com/css2?family=Cinzel:wght@400;700&family=Oswald:wght@400;500&family=Open+Sans:wght@400;600;700&display=swap" rel="stylesheet">
<style>
:root{
  --navy:#2a303c;
  --navy-deep:#232833;
  --red:#a3141b;
  --beige:#f3dcc2;
  --beige-text:#b5652b;
  --paper:#eceef2;
  --white:#ffffff;
  --muted:#b9bec8;
  --ink:#3a3f49;
  --line:#4a5262;
}
*{margin:0;padding:0;box-sizing:border-box}
html,body{width:719px;height:1200px;overflow:hidden}
body{background:var(--navy);font-family:"Open Sans",sans-serif;color:var(--white);position:relative}
.top-rule{position:absolute;top:0;left:0;width:719px;height:4px;background:var(--red)}
.site-header{position:absolute;top:4px;left:0;width:719px;height:92px;background:var(--navy)}
.brand{position:absolute;top:14px;left:205px;width:310px;border-top:1px solid var(--line);border-bottom:1px solid var(--line);text-align:center;padding:5px 0;font-family:"Cinzel",serif;font-weight:700;font-size:16px;letter-spacing:1px;color:var(--white)}
.main-nav{position:absolute;top:66px;left:0;width:719px;display:flex;justify-content:center;gap:34px;font-family:"Cinzel",serif;font-size:10px;letter-spacing:1px}
.main-nav span{color:var(--white)}
.hero{position:absolute;top:96px;left:0;width:719px;height:318px;background:linear-gradient(100deg,#3a2a22 0%,#7a5a44 25%,#c9b59c 45%,#d9d0c3 60%,#5c4636 80%,#2e241f 100%)}
.promo{position:absolute;top:414px;left:0;width:719px;height:78px;background:var(--navy-deep)}
.promo-band{position:absolute;top:10px;left:0;width:719px;height:56px;background:var(--beige);text-align:center;padding-top:10px}
.promo-title{font-family:"Oswald",sans-serif;font-size:17px;letter-spacing:1px;color:var(--beige-text)}
.promo-sub{font-size:8px;letter-spacing:1px;color:#c8956b;margin-top:2px}
.promo-badge{position:absolute;top:-4px;left:612px;width:90px;height:90px;border-radius:50%;background:var(--red);text-align:center;padding-top:20px;font-family:"Oswald",sans-serif;font-size:10px;line-height:13px;color:var(--white)}
.promo-badge strong{display:block;font-size:15px;font-weight:500;line-height:18px}
.products{position:absolute;top:510px;left:0;width:719px;height:258px}
.section-title{font-family:"Oswald",sans-serif;font-size:15px;letter-spacing:1px;color:var(--white)}
.products .section-title{position:absolute;top:10px;left:34px}
.arrows{position:absolute;top:14px;left:632px;display:flex;gap:8px}
.product-grid{position:absolute;top:42px;left:34px;display:flex;gap:22px}
.product{width:140px}
.product-photo{width:140px;height:136px;background:linear-gradient(150deg,#6b4f3c,#c7ab8a 55%,#8a6a52)}
.product-photo.alt{background:linear-gradient(150deg,#c9a26b,#e6cfa5 50%,#8d6a3e)}
.product-photo.dark{background:linear-gradient(150deg,#2f2a27,#6c5e52 55%,#2a2420)}
.product-photo.teal{background:linear-gradient(150deg,#6f8d86,#d9d6cc 50%,#5a463a)}
.product-cat{font-family:"Oswald",sans-serif;font-size:9px;margin-top:7px}
.product-name{font-size:8px;color:var(--muted);margin-top:1px}
.product-price{font-family:"Oswald",sans-serif;font-size:15px;margin-top:3px}
.testimonials{position:absolute;top:770px;left:0;width:719px;height:212px;background:var(--paper);color:var(--ink)}
.testimonials h2{position:absolute;top:14px;left:24px;font-family:"Cinzel",serif;font-weight:400;font-size:17px;letter-spacing:1px}
.testimonials .rule{position:absolute;top:42px;left:24px;width:672px;height:1px;background:#c9ccd3}
.review-row{position:absolute;top:60px;left:22px;display:flex;gap:22px}
.review{width:210px;position:relative}
.avatar{position:absolute;top:8px;left:0;width:36px;height:40px;background:linear-gradient(#9aa1ac,#5c6470)}
.review-text{margin-left:48px;border:1px solid #c9ccd3;background:var(--white);padding:6px 7px;font-size:6.6px;line-height:9px;color:#6a6f78;height:92px}
.reviewer{margin-left:48px;margin-top:8px;font-family:"Oswald",sans-serif;font-size:10px;color:var(--red)}
.reviewer-role{margin-left:48px;font-size:7.5px;color:#6a6f78}
.site-footer{position:absolute;top:982px;left:0;width:719px;height:180px;background:var(--navy)}
.footer-col{position:absolute;top:14px}
.footer-col h3{font-family:"Cinzel",serif;font-weight:400;font-size:17px;letter-spacing:1px;color:var(--white);border-bottom:1px solid var(--line);padding-bottom:5px;width:205px}
.about{left:12px}
.about p{font-size:7.5px;line-height:10px;color:var(--muted);margin-top:8px;width:190px}
.info{left:257px}
.info-links{display:grid;grid-template-columns:90px 90px;row-gap:10px;margin-top:12px;font-family:"Open Sans",sans-serif;font-weight:700;font-size:7px;color:var(--white)}
.connect{left:496px}
.social{display:flex;gap:6px;margin-top:10px;margin-left:10px}
.social span{width:20px;height:20px;border-radius:50%;background:var(--white)}
.site-bottom{position:absolute;top:1162px;left:0;width:719px;height:38px;background:var(--red);font-size:7.5px;padding:14px 0 0 12px}
</style>
</head>
<body>
<div class="top-rule"></div>
<header class="site-header">
  <div class="brand">RIDGE-MOSAIC BUILDERS &amp; INTERIORS</div>
  <nav class="main-nav"><span>HOME</span><span>ABOUT US</span><span>PRODUCTS</span><span>CONTACT US</span></nav>
</header>

<div class="hero" role="img" aria-label="Modern kitchen with stone countertop, sink and dark cabinets"></div>

<section class="promo">
  <div class="promo-band">
    <div class="promo-title">FREE SHIPPING ON ALL ORDERS OVER $150</div>
    <div class="promo-sub">NO REQUIREMENTS REQUIRED JUST SHOP ABOVE $150</div>
  </div>
  <div class="promo-badge">DELIVERED<br>TO YOUR<br>DOOR<strong>IN 3 DAYS</strong></div>
</section>

<section class="products">
  <h2 class="section-title">FEATURED PRODUCTS</h2>
  <div class="arrows">
    <svg width="9" height="10" viewBox="0 0 9 10"><path d="M8 0L0 5l8 5z" fill="#fff"/></svg>
    <svg width="9" height="10" viewBox="0 0 9 10"><path d="M1 0l8 5-8 5z" fill="#fff"/></svg>
  </div>
  <div class="product-grid">
    <div class="product"><div class="product-photo" role="img" aria-label="Kitchen with stone countertop"></div><div class="product-cat">TOPS</div><div class="product-name">Polished Quartz Vanity Top</div><div class="product-price">$103.23</div></div>
    <div class="product"><div class="product-photo alt" role="img" aria-label="Granite kitchen island"></div><div class="product-cat">TOPS</div><div class="product-name">Granite Island Countertop Slab</div><div class="product-price">$103.23</div></div>
    <div class="product"><div class="product-photo dark" role="img" aria-label="Dark marble bathroom counter"></div><div class="product-cat">TOPS</div><div class="product-name">Marble Bath Surround Set</div><div class="product-price">$103.23</div></div>
    <div class="product"><div class="product-photo teal" role="img" aria-label="Kitchen countertop with tiled backsplash"></div><div class="product-cat">TOPS</div><div class="product-name">Travertine Kitchen Top Edge</div><div class="product-price">$103.23</div></div>
  </div>
</section>

<section class="testimonials">
  <h2>TESTIMONIALS</h2>
  <div class="rule"></div>
  <div class="review-row">
    <div class="review"><div class="avatar" role="img" aria-label="Customer portrait"></div>
      <p class="review-text">Our kitchen counters came out flawless. The crew measured twice, cut clean seams and left the site spotless. I now send every buyer looking at a remodel straight to this team.</p>
      <div class="reviewer">Rafe Colden</div><div class="reviewer-role">Real Estate Guru</div></div>
    <div class="review"><div class="avatar" role="img" aria-label="Customer portrait"></div>
      <p class="review-text">Reliable tile partners are rare. They source honest stone, keep schedules tight and handle tricky shower niches with ease. My clients keep asking who did the backsplash work in their homes.</p>
      <div class="reviewer">Lina Carvo</div><div class="reviewer-role">Interior Designer</div></div>
    <div class="review"><div class="avatar" role="img" aria-label="Customer portrait"></div>
      <p class="review-text">From slab selection to final sealing, every step was explained clearly. The floors are level, grout lines are even, and the finish has held up well after a year of heavy use.</p>
      <div class="reviewer">Tobin Marsh</div><div class="reviewer-role">Civil Engineer</div></div>
  </div>
</section>

<footer class="site-footer">
  <div class="footer-col about"><h3>ABOUT US</h3>
    <p>Family owned tile and stone specialists serving homeowners with custom countertops, floors, showers and backsplashes. Every project is measured, cut and installed by our own trained crew.</p></div>
  <div class="footer-col info"><h3>INFORMATION</h3>
    <div class="info-links"><span>TRACK ORDERS</span><span>BLOG</span><span>FAQS</span><span>ABOUT US</span><span>PORTFOLIO</span><span>SERVICES</span><span>SHOP SALES</span><span>CONTACT US</span></div></div>
  <div class="footer-col connect"><h3>CONNECT</h3>
    <div class="social"><span></span><span></span><span></span><span></span><span></span><span></span></div></div>
</footer>
<div class="site-bottom">© Copyright Ridge-Mosaic Builders &amp; Interiors 2014. All Rights Reserved.</div>
</body>
</html>
```